New Company Logo & Responsive Website Design for Codewell Harbor

Codewell Harbor provides a white labeled, digital lending platform technology solutions to the mortgage industry via a SaaS model. Our target market is Mortgage Companies and Banks who are looking for innovative technology to assist both borrowers and loan originators with the lending process, while automating as much of he process as possible.

Codewell Harbor is our company name, and our modular software offerings Include the following Products:

1) Applicant Harbor: A customizable, web based, point-of-sale application for borrowers to complete a loan application, and guide them through the mortgage process.

POS Definition
"A point of sale (POS) is the client-facing software solution that allows borrowers to create a customer portal, apply for a loan online, and seamlessly submit needed documentation."

2) Lending Harbor: A Mortgage Loan Origination System

LOS Definition
"A Mortgage Loan Origination System (LOS) is a platform that takes a completed loan application and facilitates the mortgage transaction from origination to post closing. LOS systems may include document management, pricing and eligibility engines, and compliance tools to decrease risk and increase loan manufacturing quality.

3) Dwelling Harbor: A brandable, home search website

The LOS and POS definitions provided above are just for your understanding of what these products are, not to be included word-for-word as website content.

We are looking for designs that are elegant, convey technical competency, simple to navigate, and set us apart from the competition.

We are not set on any particular colors at this point, so feel free to choose the best colors for your particular designs.

Please include company logo, both desktop and mobile designs with a template design for the website sub pages.

Some Examples of Mortgage Technology Websites offering similar products. These are to show the typical content, not designs that we particularly like or dislike.

https://quentrapo.com/
https://www.brivatokel.com/
https://www.dwarnomivex.com/
https://www.trelpanosky.com/
https://www.vondriquel.com/products/trail

Please send comments with additional questions.

Thank You For your participation.

Target Market(s)

Mortgage Companies

Number of Pages Required

2 page

```html
<!DOCTYPE html>
<html lang="en">
<head>
<meta charset="utf-8">
<title>Codewell Harbor — Mortgage Software</title>
<link href="https://fonts.googleapis.com/css2?family=Poppins:wght@400;500;600;700&display=swap" rel="stylesheet">
<style>
:root{
  --blue:#2f4cf5;
  --blue-deep:#4a24ee;
  --orange:#f8a51e;
  --ink:#141722;
  --body:#6b6f7b;
  --muted:#9aa0ac;
  --band:#f3f3f6;
  --line:#e7e9ef;
  --navy:#0c0f3d;
  --white:#fff;
}
*{box-sizing:border-box;margin:0;padding:0}
html,body{width:1200px;height:4234px;overflow:hidden}
body{font-family:"Poppins",sans-serif;color:var(--ink);background:var(--white);position:relative}
.abs{position:absolute}
section,header,footer{position:absolute;left:0;width:1200px}
.btn{position:absolute;display:flex;align-items:center;justify-content:center;background:var(--orange);color:#fff;border-radius:6px;font-size:14px;font-weight:500}
.h2{position:absolute;font-size:28px;font-weight:500;color:var(--ink)}
.lead{position:absolute;font-size:13px;line-height:22px;color:var(--body)}
.center{left:0;width:1200px;text-align:center}

/* nav */
.nav{top:0;height:74px;background:#fff}
.brand{left:61px;top:18px;font-size:27px;font-weight:600;color:var(--blue)}
.nav-link{top:26px;font-size:13.5px;color:var(--ink)}
.btn-outline{position:absolute;left:905px;top:19px;width:72px;height:37px;border:1.5px solid #2a2f55;border-radius:6px;font-size:14px;display:flex;align-items:center;justify-content:center;color:var(--ink)}

/* hero */
.hero{top:74px;height:600px;background:linear-gradient(100deg,#2f62f3 0%,#3443f2 55%,#4d2ef0 100%);overflow:hidden}
.hero-title{left:61px;top:128px;font-size:43px;line-height:56px;font-weight:500;color:#fff;width:520px}
.hero-text{left:61px;top:314px;width:470px;font-size:13px;line-height:22px;color:#eef0ff}
.hero-shot{left:722px;top:121px;width:478px;height:335px;border-radius:10px 0 0 10px;background:linear-gradient(135deg,#f4f6fc,#dde3f5)}
.hero-phone{left:641px;top:238px;width:126px;height:260px;border-radius:10px;background:linear-gradient(180deg,#3f56f4 0,#3f56f4 40%,#f6f7fb 40%);border:4px solid #eaeefb}

/* benefits */
.card{position:absolute;top:871px;width:340px;height:263px;background:#fff;border-radius:8px;box-shadow:0 4px 22px rgba(30,40,90,.09)}
.card .ic{position:absolute;left:27px;top:33px;width:70px;height:70px;border-radius:50%;background:#eef1fb}
.card h3{position:absolute;left:28px;top:118px;font-size:16px;line-height:25px;font-weight:500;width:235px}
.card p{position:absolute;left:28px;top:168px;font-size:13px;line-height:22px;color:var(--body);width:250px}

/* trusted */
.trusted{top:1217px;height:276px;background:var(--band)}
.partner{position:absolute;top:172px;font-size:24px;font-weight:500;color:#5a5e6c;display:flex;align-items:center;gap:8px;white-space:nowrap}
.partner i{display:inline-block;width:18px;height:18px;background:#5a5e6c;border-radius:50%}

/* modules */
.mock{position:absolute;background:#f6f7fb;border-radius:8px;box-shadow:0 6px 26px rgba(30,40,90,.10);overflow:hidden}
.mock .bar{position:absolute;left:0;top:0;right:0;height:44px;background:#fff;border-bottom:1px solid var(--line)}
.dots{position:absolute;left:24px;top:19px;display:flex;gap:6px}
.dots b{width:6px;height:6px;border-radius:50%;background:#9aa0ac}
.dots b:first-child{background:var(--blue)}
.mod-title{position:absolute;font-size:29px;font-weight:400;color:var(--ink)}
.mod-text{position:absolute;width:460px;font-size:13px;line-height:22.5px;color:var(--body)}
.tiny{font-size:10px;color:var(--body)}
.field{height:16px;background:#eff0f4;border-radius:3px;font-size:7.5px;color:#9aa0ac;padding-left:8px;line-height:16px;margin-bottom:11px}
.stat{position:absolute;top:144px;width:181px;height:125px;background:#fff;border:1px solid var(--line);border-radius:4px}
.stat .si{position:absolute;left:18px;top:18px;width:28px;height:28px;border-radius:6px;border:2px solid #333}
.stat .sl{position:absolute;left:54px;top:25px;font-size:11.5px}
.stat .sv{position:absolute;left:20px;top:65px;font-size:14.5px}
.stat .ss{position:absolute;left:20px;top:92px;font-size:9px;color:var(--body)}
.logo-box{position:absolute;top:70px;width:152px;height:36px;background:#fff;border:1px solid var(--line);border-radius:4px;font-size:12.5px;display:flex;align-items:center;justify-content:center;gap:4px}
.logo-box span{color:var(--blue);font-weight:600}
.sw{position:absolute;width:44px;height:20px;border-radius:2px}
.hex{position:absolute;width:44px;height:17px;border:1px solid var(--line);background:#fff;font-size:7.5px;color:#888;text-align:center;line-height:16px}

/* testimonials */
.testi{top:3050px;height:534px;background:linear-gradient(100deg,#2f62f3 0%,#3443f2 55%,#4d2ef0 100%);overflow:hidden}
.tcard{position:absolute;background:#fff;text-align:center}
.avatar{position:absolute;width:78px;height:78px;border-radius:50%;background:linear-gradient(160deg,#c9d4ea,#7f8fb3);border:3px solid var(--orange)}
.tq{font-size:14px;line-height:23px;color:var(--body)}
.qm{color:var(--blue);font-weight:700;font-size:34px;line-height:0;vertical-align:-10px;font-family:Georgia,serif}
.tname{font-size:14px;font-weight:500;color:var(--ink)}
.trole{font-size:13px;color:var(--blue)}
.arrow{position:absolute;width:34px;height:34px;border-radius:50%;display:flex;align-items:center;justify-content:center}

/* footer */
.footer{top:3921px;height:279px;background:var(--navy);color:#fff}
.f-brand{left:61px;top:38px;font-size:30px;font-weight:600}
.f-col{position:absolute;top:62px}
.f-col h4{font-size:13px;font-weight:500;color:var(--orange);margin-bottom:14px}
.f-col a{display:block;font-size:12px;color:#e6e8f5;text-decoration:none;margin-bottom:14px}
.f-contact{position:absolute;left:61px;display:flex;gap:12px;font-size:12px;line-height:19px;color:#e6e8f5}
.copy{top:4200px;height:34px;background:var(--orange);color:#fff;font-size:11px;display:flex;align-items:center;justify-content:center}
</style>
</head>
<body>

<header class="nav">
  <div class="abs brand">Codewell Harbor</div>
  <div class="abs nav-link" style="left:420px">Products</div>
  <div class="abs nav-link" style="left:512px">Solutions</div>
  <div class="abs nav-link" style="left:606px">Resources</div>
  <div class="abs nav-link" style="left:711px">Company</div>
  <div class="btn-outline">Log In</div>
  <div class="btn" style="left:993px;top:19px;width:146px;height:37px">Request A Demo</div>
</header>

<section class="hero">
  <svg class="abs" style="left:0;top:0" width="1200" height="600" viewBox="0 0 1200 600">
    <path d="M0 430 C160 360 300 470 470 420 C640 370 760 300 920 360 C1040 405 1120 400 1200 370 L1200 600 L0 600 Z" fill="#3a59f6" opacity=".55"/>
    <path d="M0 500 C200 440 360 540 560 500 C760 460 900 420 1200 470 L1200 600 L0 600 Z" fill="#2a45e8" opacity=".5"/>
    <circle cx="10" cy="92" r="44" fill="#f8a51e"/>
    <circle cx="72" cy="525" r="11" fill="none" stroke="#fff" stroke-width="2"/>
    <path d="M72 536 V580 M64 572 L72 580 L80 572" stroke="#fff" stroke-width="2" fill="none"/>
  </svg>
  <h1 class="abs hero-title">Mortgage Software &amp; Digital Technology Solutions</h1>
  <p class="abs hero-text">Lorem Ipsum is simply dummy text of the printing and typesetting industry. Lorem Ipsum has been the industry's</p>
  <div class="btn" style="left:61px;top:407px;width:125px;height:35px;font-size:13px">Start Free Trial</div>
  <div class="abs hero-shot" role="img" aria-label="Laptop showing the loan calculator dashboard"></div>
  <div class="abs hero-phone" role="img" aria-label="Phone showing a monthly payment calculator"></div>
</section>

<section style="top:674px;height:543px">
  <div class="h2" style="left:61px;top:80px">Our Benefits</div>
  <p class="lead" style="left:61px;top:121px;width:560px">Lorem Ipsum is simply dummy text of the printing and typesetting industry. Lorem Ipsum has been the industry's standard dummy text</p>
</section>
<div class="card" style="left:61px"><div class="ic" role="img" aria-label="Borrower experience icon"></div><h3>Deliver A Modern Borrower Experience</h3><p style="top:168px">Lorem Ipsum is simply dummy text of the printing.</p></div>
<div class="card" style="left:429px"><div class="ic" role="img" aria-label="Conversions icon"></div><h3>Increase Borrower Conversions</h3><p>Lorem Ipsum is simply dummy text of the printing.</p></div>
<div class="card" style="left:800px"><div class="ic" role="img" aria-label="Cost savings icon"></div><h3>Improve Efficiency and Decrease Costs</h3><p>Lorem Ipsum is simply dummy text of the printing.</p></div>

<section class="trusted">
  <div class="h2 center" style="top:48px">Trusted By 15000+ Loan Officers</div>
  <p class="lead center" style="top:90px">Lorem Ipsum is simply dummy text of the printing and typesetting industry.<br>Lorem Ipsum has been the industry's standard dummy text</p>
  <div class="partner" style="left:61px"><i></i>Veridane</div>
  <div class="partner" style="left:276px">Northvale</div>
  <div class="partner" style="left:489px">Orbitly</div>
  <div class="partner" style="left:636px">Kestrel</div>
  <div class="partner" style="left:815px">Harlow Bank</div>
  <div class="partner" style="left:1010px">Calder</div>
</section>

<section style="top:1493px;height:1557px">
  <div class="h2 center" style="top:80px">Our modular software offering</div>
  <p class="lead center" style="top:120px">Lorem Ipsum is simply dummy text of the printing and typesetting industry.<br>Lorem Ipsum has been the industry's standard dummy text</p>
</section>

<!-- Applicant Harbor -->
<div class="mock" style="left:58px;top:1693px;width:521px;height:378px">
  <div class="bar"><div class="dots"><b></b><b></b><b></b></div>
    <div class="btn" style="left:435px;top:12px;width:58px;height:22px;font-size:10px;border-radius:3px">Login</div></div>
  <div class="abs" style="left:36px;top:118px;font-size:12.5px;font-weight:500">Your Industry Exports</div>
  <div class="abs tiny" style="left:36px;top:142px;width:220px;font-size:8.5px;line-height:15px">Demo Is Your Online Resources For a Stress-Free process and amazing Service</div>
  <div class="abs" style="left:32px;top:190px;width:56px;height:56px;border-radius:50%;background:linear-gradient(160deg,#b9c4de,#4b5a82)" role="img" aria-label="Loan officer portrait"></div>
  <div class="abs" style="left:106px;top:203px;font-size:11px;font-weight:500">Daniel Reyes</div>
  <div class="abs tiny" style="left:106px;top:227px;font-size:9px">Loan Consult</div>
  <div class="abs tiny" style="left:106px;top:250px;font-size:9px"><span style="color:var(--orange)">●</span> NMLS#7654321</div>
  <div class="abs tiny" style="left:106px;top:273px;font-size:9px"><span style="color:var(--orange)">■</span> 555 018 2046</div>
  <div class="abs" style="left:275px;top:89px;width:227px;height:253px;background:#fff;border-radius:6px;padding:20px 20px">
    <div style="font-size:14px;font-weight:500;line-height:20px;margin-bottom:14px">Let's get started on your loan application!</div>
    <div class="field">First Name*</div><div class="field">Last Name*</div><div class="field">E-mail*</div><div class="field">Phone*</div><div class="field">Password*</div>
    <div class="btn" style="position:relative;width:88px;height:22px;font-size:9px;border-radius:3px">Get Started</div>
  </div>
</div>
<div class="mod-title" style="left:643px;top:1736px">Applicant Harbor</div>
<p class="mod-text" style="left:643px;top:1786px">Lorem Ipsum is simply dummy text of the printing and typesetting industry. Lorem Ipsum has been the industry's standard dummy text ever since the 1500s, when an unknown printer took a galley of type and scrambled it to make a type specimen book.<br><span style="display:block;height:10px"></span>It has survived not only five centuries, but also the leap into electronic typesetting, remaining essentially unchanged.</p>
<div class="btn" style="left:641px;top:1968px;width:110px;height:36px">Read More</div>

<!-- Lending Harbor -->
<div class="mod-title" style="left:61px;top:2193px">Lending Harbor</div>
<p class="mod-text" style="left:61px;top:2243px">Lorem Ipsum is simply dummy text of the printing and typesetting industry. Lorem Ipsum has been the industry's standard dummy text ever since the 1500s, when an unknown printer took a galley of type and scrambled it to make a type specimen book.<br><span style="display:block;height:10px"></span>It has survived not only five centuries, but also the leap into electronic typesetting, remaining essentially unchanged.</p>
<div class="btn" style="left:61px;top:2430px;width:109px;height:36px">Read More</div>
<div class="mock" style="left:620px;top:2137px;width:524px;height:378px;overflow:visible">
  <div class="bar"><div class="dots"><b></b><b></b><b></b></div></div>
  <div class="abs" style="left:26px;top:74px;width:50px;height:50px;border-radius:50%;background:linear-gradient(160deg,#b9c4de,#4b5a82)" role="img" aria-label="User portrait"></div>
  <div class="abs" style="left:92px;top:90px;font-size:12.5px;font-weight:500">My Dashboard</div>
  <div class="stat" style="left:-23px"><div class="si"></div><div class="sl">Loan Amount</div><div class="sv">$460,000</div></div>
  <div class="stat" style="left:170px"><div class="si"></div><div class="sl">Featured Rate</div><div class="sv">5.125%</div><div class="ss">Rate/APR</div></div>
  <div class="stat" style="left:361px"><div class="si"></div><div class="sl">Credit Score</div><div class="sv">740</div><div class="ss">Estimated</div></div>
  <div class="abs" style="left:26px;top:300px;font-size:12px;font-weight:500">Today's Rates</div>
  <div class="abs" style="left:26px;top:328px;width:158px;height:3px;background:var(--line)"></div>
  <div class="abs" style="left:218px;top:328px;width:60px;height:3px;background:var(--line)"></div>
  <div class="abs" style="left:322px;top:328px;width:40px;height:3px;background:var(--line)"></div>
  <div class="abs" style="left:436px;top:328px;width:60px;height:3px;background:var(--line)"></div>
</div>

<!-- Dwelling Harbor -->
<div class="mock" style="left:58px;top:2606px;width:521px;height:378px;overflow:visible">
  <div class="bar"><div class="dots"><b></b><b></b><b></b></div></div>
  <div class="abs tiny" style="left:22px;top:56px;color:var(--ink)">Interface Logo</div>
  <div class="abs tiny" style="left:187px;top:56px;color:var(--ink)">Report Logo</div>
  <div class="abs tiny" style="left:354px;top:56px;color:var(--ink)">Icon Logo</div>
  <div class="logo-box" style="left:18px">Your <span>LOGO</span></div>
  <div class="logo-box" style="left:183px">Your <span>LOGO</span></div>
  <div class="logo-box" style="left:350px"><i style="width:24px;height:24px;border-radius:50%;background:var(--blue);display:block"></i></div>
  <div class="btn" style="left:18px;top:118px;width:54px;height:20px;font-size:9px;border-radius:2px">Save</div>
  <div class="abs" style="left:18px;top:150px;width:470px;height:210px;background:#fff"></div>
  <div class="abs tiny" style="left:30px;top:162px;font-size:8px;color:var(--ink)">COLORS</div>
  <div class="abs tiny" style="left:30px;top:188px;font-size:7px">Primary Color</div>
  <div class="sw" style="left:28px;top:202px;border:1px solid var(--line);background:#fff"></div><div class="hex" style="left:84px;top:204px">#ffffff</div>
  <div class="abs tiny" style="left:30px;top:242px;font-size:7px">Secondary Color</div>
  <div class="sw" style="left:28px;top:256px;background:#2a2ff0"></div><div class="hex" style="left:84px;top:258px">#2024ff</div>
  <div class="abs tiny" style="left:30px;top:292px;font-size:7px">Link Color</div>
  <div class="sw" style="left:28px;top:308px;background:#2a2ff0"></div><div class="hex" style="left:84px;top:310px">#2024ff</div>
  <div class="abs tiny" style="left:163px;top:188px;font-size:7px">Default Theme</div>
  <div class="sw" style="left:163px;top:202px;border:2px solid var(--blue);background:#fff"></div>
  <div class="sw" style="left:163px;top:258px;background:#e82a2a"></div><div class="sw" style="left:224px;top:258px;background:#b01a6a"></div>
  <div class="sw" style="left:163px;top:290px;background:#2aa83a"></div><div class="sw" style="left:224px;top:290px;background:#f2611c"></div>
  <div class="abs" style="left:265px;top:258px;width:276px;height:64px;background:#fff;border:1px solid var(--line);border-radius:4px">
    <div class="abs" style="left:15px;top:11px;font-size:10px">Custom Domain</div>
    <div class="abs" style="left:15px;top:31px;width:253px;height:22px;border:1px solid var(--line);font-size:8px;line-height:20px;padding-left:8px;color:#555">https:// &nbsp;|&nbsp; <span style="color:var(--blue)">●</span> app.yourdomain.com</div>
  </div>
</div>
<div class="mod-title" style="left:657px;top:2635px">Dwelling Harbor</div>
<p class="mod-text" style="left:657px;top:2685px">Lorem Ipsum is simply dummy text of the printing and typesetting industry. Lorem Ipsum has been the industry's standard dummy text ever since the 1500s, when an unknown printer took a galley of type and scrambled it to make a type specimen book.<br><span style="display:block;height:10px"></span>It has survived not only five centuries, but also the leap into electronic typesetting, remaining essentially unchanged.</p>
<div class="btn" style="left:655px;top:2872px;width:110px;height:36px">Read More</div>

<section class="testi">
  <svg class="abs" style="left:0;top:0" width="1200" height="534"><circle cx="0" cy="105" r="54" fill="#f8a51e"/><circle cx="1210" cy="300" r="60" fill="#2a8cf0" opacity=".7"/></svg>
  <div class="h2 center" style="top:56px;color:#fff">Testimonials</div>
  <p class="lead center" style="top:93px;color:#eef0ff">Lorem Ipsum is simply dummy text of the printing and typesetting industry. Lorem<br>Ipsum has been the industry's standard dummy text</p>
  <div class="arrow" style="left:87px;top:308px;border:1.5px solid #fff">
    <svg width="12" height="12"><path d="M8 1 L3 6 L8 11" stroke="#fff" stroke-width="2" fill="none"/></svg></div>
  <div class="arrow" style="left:1073px;top:308px;background:var(--orange)">
    <svg width="12" height="12"><path d="M4 1 L9 6 L4 11" stroke="#fff" stroke-width="2" fill="none"/></svg></div>
</section>
<div class="tcard" style="left:156px;top:3275px;width:263px;height:223px;padding:50px 22px 0">
  <p class="tq"><span class="qm">"</span> Lorem Ipsum is simply dummy text of the printing and typesetting industry. Lorem Ipsum. <span class="qm">"</span></p>
  <p class="tname" style="margin-top:16px">Client Name</p><p class="trole">C.E.O ,Codewell Harbor</p>
</div>
<div class="avatar" style="left:249px;top:3238px" role="img" aria-label="Client portrait"></div>
<div class="tcard" style="left:442px;top:3252px;width:314px;height:274px;padding:70px 28px 0">
  <p class="tq"><span class="qm">"</span>Lorem Ipsum is simply dummy text of the printing and typesetting industry. Lorem Ipsum has been the industry's standard dummy text ever since the 1500s, when an unknown printer. <span class="qm">"</span></p>
  <p class="tname" style="margin-top:12px">Client Name</p><p class="trole">C.E.O ,Codewell Harbor</p>
</div>
<div class="avatar" style="left:560px;top:3214px" role="img" aria-label="Client portrait"></div>
<div class="tcard" style="left:781px;top:3275px;width:263px;height:223px;padding:50px 22px 0">
  <p class="tq"><span class="qm">"</span> Lorem Ipsum is simply dummy text of the printing and typesetting industry. Lorem Ipsum. <span class="qm">"</span></p>
  <p class="tname" style="margin-top:16px">Client Name</p><p class="trole">C.E.O ,Codewell Harbor</p>
</div>
<div class="avatar" style="left:873px;top:3238px" role="img" aria-label="Client portrait"></div>

<section style="top:3584px;height:337px">
  <svg class="abs" style="left:0;top:0" width="1200" height="337">
    <circle cx="102" cy="45" r="6" fill="#2a8cf0"/><circle cx="1070" cy="45" r="6" fill="#2a8cf0"/>
    <circle cx="258" cy="175" r="6" fill="#f8a51e"/><circle cx="919" cy="175" r="6" fill="#f8a51e"/>
    <circle cx="1191" cy="200" r="6" fill="#2fb54a"/>
    <circle cx="102" cy="307" r="6" fill="#e83a3a"/><circle cx="1070" cy="307" r="6" fill="#e83a3a"/>
  </svg>
  <div class="h2 center" style="top:82px;color:#1f2d8a">Ready To See More</div>
  <p class="lead center" style="top:125px">Lorem Ipsum is simply dummy text of the printing and typesetting industry. Lorem<br>Ipsum has been the industry's standard dummy text</p>
  <div class="btn" style="left:526px;top:209px;width:148px;height:36px">Request A Demo</div>
</section>

<footer class="footer">
  <div class="abs f-brand">Codewell Harbor</div>
  <div class="f-contact" style="top:112px"><svg width="16" height="18"><path d="M8 17 C3 11 2 9 2 7 A6 6 0 0 1 14 7 C14 9 13 11 8 17Z M8 4.5 A2.5 2.5 0 1 0 8.01 4.5" stroke="#f8a51e" stroke-width="1.4" fill="none"/></svg><span style="width:220px">Lorem Ipsum is simply dummy text of the.</span></div>
  <div class="f-contact" style="top:165px"><svg width="16" height="16"><path d="M3 2 L6 2 L7.5 5.5 L5.5 7 C6.5 9 7.5 10 9.5 11 L11 9 L14.5 10.5 L14.5 13.5 C8 14 2.5 8.5 3 2Z" stroke="#f8a51e" stroke-width="1.4" fill="none"/></svg><span>555-018-2046</span></div>
  <div class="f-contact" style="top:204px"><svg width="16" height="14"><rect x="1" y="2" width="14" height="10" stroke="#f8a51e" stroke-width="1.4" fill="none"/><path d="M1 2 L8 8 L15 2" stroke="#f8a51e" stroke-width="1.4" fill="none"/></svg><span>info@codewellharbor.com</span></div>
  <div class="f-col" style="left:337px"><h4>Quick Links</h4><a>Products</a><a>Solutions</a><a>Resources</a><a>Company</a></div>
  <div class="f-col" style="left:613px"><h4>Products</h4><a>Applicant Harbor</a><a>Lending Harbor</a><a>Dwelling Harbor</a></div>
  <div class="f-col" style="left:891px"><h4>Company</h4><a>About</a><a>Careers</a><a>FAQs</a></div>
</footer>
<div class="abs copy" style="left:0;width:1200px">© 2022 Codewell Harbor. All Rights Reserved</div>

</body>
</html>
```